Criação de Papelaria Profissional para Logística, Entrega & Armazenamento
A empresa queria:
" Somos a evolução do Self Storage. Buscamos , armazenamos, levamos de volta , tendo tudo que está armazenado com fotos no sistema, sendo tudo feito pela internet. "

```html
<!DOCTYPE html>
<html lang="pt-BR">
<head>
<meta charset="utf-8">
<title>StoraNet – Envelope</title>
<link rel="stylesheet" href="https://fonts.googleapis.com/css2?family=Montserrat:wght@500;800&display=swap">
<style>
  :root {
    --bg: #e8e5e1;
    --brand-blue: #2fb0e6;
    --brand-blue-light: #5cc3ee;
    --paper: #ffffff;
    --paper-shade: #eef0f2;
    --ink: #141414;
    --ink-on-blue: #ffffff;
  }
  html, body {
    margin: 0;
    padding: 0;
    width: 1200px;
    height: 1200px;
    overflow: hidden;
    background: var(--bg);
  }
  .stationery { display: block; width: 1200px; height: 1200px; }
  .envelope-front .flap,
  .envelope-front .base-band { fill: var(--brand-blue); }
  .envelope-front .body { fill: var(--paper); }
  .envelope-back .body { fill: var(--brand-blue); }
  .envelope-back .flap-inner { fill: var(--paper-shade); }
  .envelope-back .flap-edge { fill: var(--paper); }
  .brand-mark { fill: var(--ink); }
  .brand-name {
    font-family: "Montserrat", sans-serif;
    font-weight: 800;
    fill: var(--ink);
  }
  .brand-name.on-blue { fill: var(--ink-on-blue); }
  .brand-mark.on-blue { fill: var(--ink-on-blue); }
  .contact-text {
    font-family: "Montserrat", sans-serif;
    font-weight: 500;
    font-size: 9px;
    fill: var(--ink-on-blue);
  }
  .contact-icon { fill: none; stroke: var(--ink-on-blue); stroke-width: 1.3; }
  .side-strip { fill: var(--paper); }
</style>
</head>
<body>
<svg class="stationery" viewBox="0 0 1200 1200" xmlns="http://www.w3.org/2000/svg">
  <defs>
    <linearGradient id="decor-tone" x1="0" y1="0" x2="1" y2="1">
      <stop offset="0" stop-color="#3db6e9"/>
      <stop offset="1" stop-color="#36b2e7"/>
    </linearGradient>
  </defs>

  <!-- Envelope: front face -->
  <g class="envelope-front">
    <path class="flap" d="M103 252 H559 Q567 252 568 262 L571 336 H91 L94 262 Q95 252 103 252 Z"/>
    <rect class="body" x="91" y="334" width="480" height="794"/>
    <rect class="base-band" x="91" y="1066" width="480" height="62"/>
    <g class="brand-lockup" transform="translate(175 690)">
      <rect class="brand-mark" x="0" y="0" width="54" height="54" rx="6"/>
      <text class="brand-name" x="70" y="43" font-size="50">StoraNet</text>
    </g>
  </g>

  <!-- Envelope: back face -->
  <g class="envelope-back">
    <rect class="body" x="614" y="330" width="478" height="798"/>
    <path class="flap-edge" d="M626 252 H1080 Q1088 252 1089 262 L1092 336 H614 L617 262 Q618 252 626 252 Z"/>
    <path class="flap-inner" d="M626 262 H1080 L1084 330 H622 Z"/>
    <rect x="650" y="520" width="410" height="390" fill="url(#decor-tone)"
          role="img" aria-label="Faint outline of the brand's open-box symbol as background decoration"/>
    <rect class="side-strip" x="620" y="985" width="8" height="120"/>

    <g class="contact-block" transform="translate(642 985)">
      <g transform="translate(0 0)">
        <path class="contact-icon" d="M1 2 Q1 1 3 1 L5 1 L6 4 L4.5 5 Q6 8 8 9.5 L9 8 L12 9 L12 11 Q12 12 11 12 Q1 11 1 2 Z"/>
        <text class="contact-text" x="20" y="10">(11) 4000-1234</text>
      </g>
      <g transform="translate(0 28)">
        <rect class="contact-icon" x="0.5" y="2" width="12" height="9" rx="1"/>
        <path class="contact-icon" d="M0.5 2.5 L6.5 7 L12.5 2.5"/>
        <text class="contact-text" x="20" y="10">contato@storanet.com.br</text>
      </g>
      <g transform="translate(0 56)">
        <circle class="contact-icon" cx="6.5" cy="6.5" r="6"/>
        <path class="contact-icon" d="M0.5 6.5 H12.5 M6.5 0.5 Q2 6.5 6.5 12.5 Q11 6.5 6.5 0.5"/>
        <text class="contact-text" x="20" y="10">www.storanet.com.br</text>
      </g>
      <g transform="translate(0 84)">
        <path class="contact-icon" d="M6.5 13 Q1 7 1 5 A5.5 5.5 0 0 1 12 5 Q12 7 6.5 13 Z"/>
        <circle class="contact-icon" cx="6.5" cy="5" r="2"/>
        <text class="contact-text" x="20" y="10">Rua das Caixas, 250 – São Paulo</text>
      </g>
    </g>

    <g class="brand-lockup" transform="translate(952 1030)">
      <rect class="brand-mark on-blue" x="0" y="0" width="20" height="20" rx="2"/>
      <text class="brand-name on-blue" x="26" y="17" font-size="19">StoraNet</text>
    </g>
  </g>
</svg>
</body>
</html>
```